Coral Ridge Pools New website

I currently operate a swimming pool service and repair business and looking for a re design for my website as it has been over 5 years since it was designed. current site is coralridgepoolsqx.com

```html
<!DOCTYPE html>
<html lang="en">
<head>
<meta charset="utf-8">
<title>Coral Ridge Pools</title>
<link href="https://fonts.googleapis.com/css2?family=Poppins:wght@400;500;600;700&family=Great+Vibes&family=Playfair+Display:wght@700&display=swap" rel="stylesheet">
<style>
:root{
  --blue:#0b5a9c;
  --blue-deep:#084a82;
  --orange:#f9a826;
  --ink:#222;
  --muted:#444;
  --white:#fff;
  --pool-light:#7fd6ec;
  --pool:#1aa6d4;
  --leaf:#5d8f4a;
}
*{margin:0;padding:0;box-sizing:border-box}
html,body{width:1200px;height:5042px;overflow:hidden}
body{position:relative;font-family:"Poppins",sans-serif;color:var(--ink);background:var(--white)}
.abs{position:absolute}
.script{font-family:"Great Vibes",cursive;color:var(--orange)}
.btn{position:absolute;display:flex;align-items:center;justify-content:center;gap:10px;background:var(--orange);color:var(--white);border-radius:30px;font-weight:500;text-transform:uppercase}
.btn svg{width:18px;height:18px}
.btn-blue{background:var(--blue)}

/* header & hero */
.hero-photo{left:0;top:0;width:1200px;height:965px;background:linear-gradient(180deg,#e9efe8 0%,#a9c79a 14%,var(--leaf) 30%,#d6b58a 40%,var(--pool-light) 48%,var(--pool) 70%,#0f8fc4 100%)}
.nav{left:0;top:36px;width:1200px;height:72px;background:var(--blue)}
.nav a{position:absolute;top:26px;color:var(--white);font-size:13px;text-decoration:none;text-transform:uppercase;font-weight:500}
.nav a.active{color:#8fd3ff}
.nav .nav-cta{top:18px;background:var(--orange);padding:9px 18px;border-radius:20px}
.brand-badge{left:470px;top:20px;width:260px;height:176px}
.brand-name{left:470px;top:86px;width:260px;text-align:center;font-size:20px;font-weight:700;color:var(--blue);line-height:1.1}
.hero-pill{left:63px;top:542px;width:1076px;height:338px;border-radius:170px;background:rgba(11,90,156,.78)}
.hero-welcome{left:0;top:582px;width:1200px;text-align:center;font-size:64px;color:var(--white)}
.hero-title{left:0;top:660px;width:1200px;text-align:center;font-family:"Playfair Display",serif;font-size:90px;color:var(--white);letter-spacing:1px}
.hero-sub{left:0;top:768px;width:1200px;text-align:center;font-size:38px;font-weight:600;color:var(--white)}

/* section headings */
.eyebrow{font-size:34px}
.h2{font-size:46px;font-weight:500;color:var(--blue);text-transform:uppercase}
.center{left:0;width:1200px;text-align:center}

/* about */
.about-text{left:642px;top:1327px;width:500px;font-size:13.4px;line-height:24px;color:var(--muted);text-align:justify}

/* services */
.service-title{font-size:31px;font-weight:600;color:var(--blue);text-align:center;line-height:38px;width:340px}
.service-rule{width:50px;height:3px;background:var(--blue)}
.service-copy{font-size:13.4px;line-height:24px;color:var(--muted);text-align:center;width:280px}

/* why */
.why-band{left:0;top:2677px;width:836px;height:619px;background:var(--blue)}
.why-label{color:var(--white);font-size:15px;text-align:center;line-height:19px}

/* blog */
.blog-photo{width:268px;height:270px;border-radius:26px 26px 0 26px}
.blog-info{background:var(--white);width:210px;height:180px;border-radius:20px 0 0 0;padding:14px 0 0 18px}
.blog-date{font-size:11px;display:flex;align-items:center;gap:8px;color:var(--ink)}
.blog-title{font-size:16px;font-weight:500;color:var(--blue);line-height:20px;margin-top:10px}
.blog-copy{font-size:13px;color:var(--muted);line-height:19px;margin-top:12px}
.blog-info .btn{position:relative;display:inline-flex;margin-top:12px;padding:6px 14px;font-size:12px}
.slider-arrow{width:30px;height:30px;border-radius:50%;display:flex;align-items:center;justify-content:center}

/* contact */
.field{position:absolute;border:1px solid #b9b9b9;font-size:12px;color:var(--muted);padding:10px 18px}

/* footer */
.footer{left:0;top:4673px;width:1200px;height:369px;background:var(--blue)}
.footer-item{display:flex;align-items:center;gap:12px;color:var(--white);font-size:13px;line-height:17px}
.footer-rule{left:64px;width:1066px;height:1px;background:rgba(255,255,255,.6)}
.footer-links{left:0;top:4908px;width:1200px;display:flex;justify-content:center;gap:38px;color:var(--white);font-size:13px;font-weight:500}
.social{width:26px;height:26px;background:var(--white);border-radius:4px}
</style>
</head>
<body>

<!-- hero -->
<div class="abs hero-photo" role="img" aria-label="Resort swimming pool with loungers, umbrellas and tropical trees"></div>
<nav class="abs nav">
  <a class="active" style="left:126px">Home</a>
  <a style="left:207px">About Us</a>
  <a style="left:313px">Our Services</a>
  <a style="left:787px">Blog</a>
  <a style="left:866px">Free Estimate</a>
  <a class="nav-cta" style="left:985px">Contact Us</a>
</nav>
<svg class="abs brand-badge" viewBox="0 0 260 176">
  <polygon points="130,8 250,88 130,168 10,88" fill="#fff" stroke="var(--orange)" stroke-width="10" stroke-linejoin="round"/>
  <polygon points="130,20 234,88 130,156 26,88" fill="#fff" stroke="var(--blue)" stroke-width="4" stroke-linejoin="round"/>
</svg>
<div class="abs brand-name">Coral Ridge<br>Pools</div>

<div class="abs hero-pill"></div>
<div class="abs script hero-welcome" style="color:#fff">Welcome To</div>
<h1 class="abs hero-title">CORAL RIDGE POOLS</h1>
<div class="abs hero-sub">NEVADA’S FIVE STAR LOCAL POOL CLEANING</div>
<div class="btn" style="left:472px;top:842px;width:254px;height:64px;font-size:22px">Free Estimate
  <svg viewBox="0 0 20 20" fill="none" stroke="#fff" stroke-width="2"><path d="M3 10h12M11 5l5 5-5 5"/></svg></div>

<!-- about -->
<svg class="abs" style="left:24px;top:1121px" width="540" height="450" viewBox="0 0 540 450" role="img" aria-label="Pool with stepping stones and garden">
  <defs><linearGradient id="gAbout" x1="0" y1="0" x2="0" y2="1"><stop offset="0" stop-color="#6f9b5a"/><stop offset=".45" stop-color="#a8e3ef"/><stop offset="1" stop-color="#4fc0df"/></linearGradient></defs>
  <polygon points="270,8 532,225 270,442 8,225" fill="#fff" stroke="var(--orange)" stroke-width="10" stroke-linejoin="round"/>
  <polygon points="270,24 512,225 270,426 28,225" fill="url(#gAbout)" stroke="var(--blue)" stroke-width="6" stroke-linejoin="round"/>
</svg>
<div class="abs script eyebrow" style="left:642px;top:1116px">About Us •••</div>
<h2 class="abs h2" style="left:642px;top:1156px">Coral Ridge Pools</h2>
<div class="abs" style="left:642px;top:1232px;width:520px;font-size:26px;line-height:34px">We are a full service pool company servicing the Las Vegas Valley</div>
<p class="abs about-text">When you need professional pool cleaning services in Nevada, you can count on the professionals at Coral Ridge Pools to provide you with superior and prompt solutions. Whether you need assistance with a residential or commercial pool, we’ll vacuum, brush, and thoroughly clean your pool so it’s swim-ready. We’ll also clean your pool filters and inform you of any issues that arise. Our staff is certified by the Desert Valley Health District to ensure proper chemical levels and equipment are safe.</p>
<div class="btn" style="left:634px;top:1518px;width:202px;height:52px;font-size:17px">Learn More
  <svg viewBox="0 0 20 20" fill="none" stroke="#fff" stroke-width="2"><path d="M3 10h12M11 5l5 5-5 5"/></svg></div>

<!-- services -->
<div class="abs script eyebrow center" style="top:1742px">••• What We Do •••</div>
<h2 class="abs h2 center" style="top:1786px">Our Services</h2>
<p class="abs center" style="top:1869px;font-size:13.4px;color:var(--muted)">We’re certified by the Desert Valley Health District to maintain proper chemical levels and operate equipment in a safe manner.</p>

<svg width="0" height="0" class="abs"><defs>
  <filter id="soft" x="-20%" y="-20%" width="140%" height="140%"><feDropShadow dx="0" dy="4" stdDeviation="8" flood-opacity=".18"/></filter>
  <linearGradient id="gPool" x1="0" y1="0" x2="1" y2="1"><stop offset="0" stop-color="#35b8e6"/><stop offset="1" stop-color="#0d7fc0"/></linearGradient>
  <linearGradient id="gFamily" x1="0" y1="0" x2="0" y2="1"><stop offset="0" stop-color="#8fd6ee"/><stop offset=".6" stop-color="#e7b98f"/><stop offset="1" stop-color="#f3d34a"/></linearGradient>
  <linearGradient id="gComm" x1="0" y1="0" x2="0" y2="1"><stop offset="0" stop-color="#c9c2b2"/><stop offset=".45" stop-color="#3aa9dd"/><stop offset="1" stop-color="#1b8fc8"/></linearGradient>
</defs></svg>

<svg class="abs" style="left:65px;top:1960px" width="340" height="300" role="img" aria-label="Pool skimmer net in clear blue water">
  <polygon points="170,14 326,150 170,286 14,150" fill="#fff" stroke="#fff" stroke-width="22" stroke-linejoin="round" filter="url(#soft)"/>
  <polygon points="170,22 316,150 170,278 24,150" fill="url(#gPool)" stroke-linejoin="round"/>
</svg>
<svg class="abs" style="left:429px;top:1960px" width="340" height="300" role="img" aria-label="Commercial pool with steel ladder">
  <polygon points="170,14 326,150 170,286 14,150" fill="#fff" stroke="#fff" stroke-width="22" stroke-linejoin="round" filter="url(#soft)"/>
  <polygon points="170,22 316,150 170,278 24,150" fill="url(#gComm)"/>
</svg>
<svg class="abs" style="left:795px;top:1960px" width="340" height="300" role="img" aria-label="Family relaxing on a pool float">
  <polygon points="170,14 326,150 170,286 14,150" fill="#fff" stroke="#fff" stroke-width="22" stroke-linejoin="round" filter="url(#soft)"/>
  <polygon points="170,22 316,150 170,278 24,150" fill="url(#gFamily)"/>
</svg>

<div class="abs service-title" style="left:65px;top:2274px">POOL SERVICES</div>
<div class="abs service-rule" style="left:210px;top:2320px"></div>
<p class="abs service-copy" style="left:95px;top:2334px">When you invested in your pool, you knew it was a long-term investment in both money and time</p>

<div class="abs service-title" style="left:429px;top:2272px">COMMERCIAL<br>POOL SERVICES</div>
<div class="abs service-rule" style="left:574px;top:2355px"></div>
<p class="abs service-copy" style="left:459px;top:2369px">As a commercial property owner or manager, doing your job well requires</p>

<div class="abs service-title" style="left:795px;top:2268px">RESIDENTIAL<br>POOL SERVICES</div>
<div class="abs service-rule" style="left:940px;top:2351px"></div>
<p class="abs service-copy" style="left:825px;top:2365px">Here in Southern Nevada, you know it can get really, really hot. That’s why you</p>

<div class="btn" style="left:161px;top:2426px;width:150px;height:40px;font-size:12px">Learn More<svg viewBox="0 0 20 20" fill="none" stroke="#fff" stroke-width="2"><path d="M3 10h12M11 5l5 5-5 5"/></svg></div>
<div class="btn" style="left:525px;top:2426px;width:150px;height:40px;font-size:12px">Learn More<svg viewBox="0 0 20 20" fill="none" stroke="#fff" stroke-width="2"><path d="M3 10h12M11 5l5 5-5 5"/></svg></div>
<div class="btn" style="left:891px;top:2426px;width:150px;height:40px;font-size:12px">Learn More<svg viewBox="0 0 20 20" fill="none" stroke="#fff" stroke-width="2"><path d="M3 10h12M11 5l5 5-5 5"/></svg></div>

<!-- why choose us -->
<div class="abs why-band"></div>
<svg class="abs" style="left:481px;top:2677px" width="719" height="619" viewBox="0 0 719 619" role="img" aria-label="Hotel pool with handrails and lounge chairs">
  <defs><linearGradient id="gWhy" x1="0" y1="0" x2="0" y2="1"><stop offset="0" stop-color="#e8ecea"/><stop offset=".35" stop-color="#8fc6b6"/><stop offset=".5" stop-color="#3db4e4"/><stop offset="1" stop-color="#1584c6"/></linearGradient></defs>
  <polygon points="358,16 704,309 358,602 14,309" fill="url(#gWhy)" stroke="rgba(255,255,255,.75)" stroke-width="26" stroke-linejoin="round"/>
</svg>
<div class="abs script" style="left:66px;top:2740px;font-size:30px">Coral Ridge Pools •••</div>
<h2 class="abs" style="left:66px;top:2784px;font-size:46px;font-weight:500;color:#fff">WHY CHOOSE US?</h2>
<div class="abs" style="left:70px;top:2858px;font-size:20px;color:#fff">Our full-service pool company proudly</div>

<svg width="0" height="0" class="abs"><defs>
  <g id="whyIcon">
    <polygon points="44,4 84,44 44,84 4,44" fill="#fff" stroke="var(--orange)" stroke-width="4" stroke-linejoin="round"/>
    <circle cx="44" cy="44" r="17" fill="none" stroke="var(--blue)" stroke-width="3"/>
    <path d="M36 44l6 6 10-12" fill="none" stroke="var(--blue)" stroke-width="3" stroke-linecap="round" stroke-linejoin="round"/>
  </g>
</defs></svg>
<svg class="abs" style="left:89px;top:2917px" width="88" height="88"><use href="#whyIcon"/></svg>
<svg class="abs" style="left:314px;top:2917px" width="88" height="88"><use href="#whyIcon"/></svg>
<svg class="abs" style="left:89px;top:3074px" width="88" height="88"><use href="#whyIcon"/></svg>
<svg class="abs" style="left:314px;top:3074px" width="88" height="88"><use href="#whyIcon"/></svg>
<div class="abs why-label" style="left:43px;top:3012px;width:180px">Serves the entire<br>Las Vegas valley</div>
<div class="abs why-label" style="left:248px;top:3004px;width:220px">We’re certified by the<br>Desert Valley Health<br>District</div>
<div class="abs why-label" style="left:43px;top:3160px;width:180px">Maintain the<br>highest level of<br>pool safety</div>
<div class="abs why-label" style="left:258px;top:3162px;width:200px">Repairs, maintenance,<br>or any other pool<br>services</div>

<!-- blog -->
<div class="abs script eyebrow center" style="top:3396px">•••News&amp; Updates•••</div>
<h2 class="abs h2 center" style="top:3440px">Latest Blog</h2>

<div class="abs slider-arrow" style="left:50px;top:3709px;background:#ddd"><svg width="12" height="12" viewBox="0 0 12 12" fill="none" stroke="#555" stroke-width="2"><path d="M8 2L4 6l4 4"/></svg></div>
<div class="abs slider-arrow" style="left:1116px;top:3709px;background:var(--orange)"><svg width="12" height="12" viewBox="0 0 12 12" fill="none" stroke="#fff" stroke-width="2"><path d="M4 2l4 4-4 4"/></svg></div>

<div class="abs blog-photo" style="left:117px;top:3581px;background:linear-gradient(180deg,#9a7a4e 0%,#c9b08a 35%,#7fc7df 60%,#e9f2f5 100%)" role="img" aria-label="Resort pool with thatched umbrellas"></div>
<div class="abs blog-info" style="left:184px;top:3777px">
  <div class="blog-date"><svg width="14" height="14" viewBox="0 0 14 14"><rect x="1" y="2" width="12" height="11" rx="1" fill="none" stroke="var(--orange)" stroke-width="1.5"/><path d="M1 5h12" stroke="var(--orange)" stroke-width="1.5"/></svg>18 March 2025</div>
  <div class="blog-title">Lorem ipsum dolor sit ame etconsectetur</div>
  <div class="blog-copy">Lorem ipsum dolor sit amet, consectetur adip</div>
  <div class="btn btn-blue">Read More</div>
</div>

<div class="abs blog-photo" style="left:460px;top:3581px;background:linear-gradient(180deg,#d9ecf2 0%,#6aa05a 45%,#3c7d3a 60%,#5fc6e6 100%)" role="img" aria-label="Pool among palm trees"></div>
<div class="abs blog-info" style="left:527px;top:3777px">
  <div class="blog-date"><svg width="14" height="14" viewBox="0 0 14 14"><rect x="1" y="2" width="12" height="11" rx="1" fill="none" stroke="var(--orange)" stroke-width="1.5"/><path d="M1 5h12" stroke="var(--orange)" stroke-width="1.5"/></svg>18 March 2025</div>
  <div class="blog-title">Lorem ipsum dolor sit ame etconsectetur</div>
  <div class="blog-copy">Lorem ipsum dolor sit amet, consectetur adip</div>
  <div class="btn btn-blue">Read More</div>
</div>

<div class="abs blog-photo" style="left:798px;top:3581px;background:linear-gradient(180deg,#6fa05a 0%,#2f7fc9 35%,#1f6fc0 70%,#2a8bd6 100%)" role="img" aria-label="Pool ladder over blue tiles"></div>
<div class="abs blog-info" style="left:865px;top:3777px">
  <div class="blog-date"><svg width="14" height="14" viewBox="0 0 14 14"><rect x="1" y="2" width="12" height="11" rx="1" fill="none" stroke="var(--orange)" stroke-width="1.5"/><path d="M1 5h12" stroke="var(--orange)" stroke-width="1.5"/></svg>18 March 2025</div>
  <div class="blog-title">Lorem ipsum dolor sit ame etconsectetur</div>
  <div class="blog-copy">Lorem ipsum dolor sit amet, consectetur adip</div>
  <div class="btn btn-blue">Read More</div>
</div>

<!-- contact -->
<svg class="abs" style="left:0;top:4130px" width="600" height="530" viewBox="0 0 600 530" role="img" aria-label="Pool with steel ladder and palm trees">
  <defs><linearGradient id="gContact" x1="0" y1="0" x2="0" y2="1"><stop offset="0" stop-color="#6c9a4e"/><stop offset=".4" stop-color="#2aa2d8"/><stop offset="1" stop-color="#1a7fc4"/></linearGradient></defs>
  <polygon points="300,8 592,265 300,522 8,265" fill="#fff" stroke="var(--blue)" stroke-width="6" stroke-linejoin="round"/>
  <polygon points="300,28 568,265 300,502 32,265" fill="url(#gContact)" stroke-linejoin="round"/>
</svg>
<div class="abs script eyebrow" style="left:638px;top:4198px">Contact Us •••</div>
<h2 class="abs h2" style="left:638px;top:4236px">Coral Ridge Pools</h2>
<div class="field" style="left:644px;top:4331px;width:237px;height:40px">Your Name</div>
<div class="field" style="left:890px;top:4331px;width:236px;height:40px">Phone Number</div>
<div class="field" style="left:644px;top:4385px;width:482px;height:40px">Email Address</div>
<div class="field" style="left:644px;top:4434px;width:482px;height:80px">Message</div>
<div class="btn" style="left:644px;top:4562px;width:160px;height:52px;font-size:17px">Submit<svg viewBox="0 0 20 20" fill="none" stroke="#fff" stroke-width="2"><path d="M3 10h12M11 5l5 5-5 5"/></svg></div>

<!-- footer -->
<footer class="abs footer"></footer>
<svg class="abs" style="left:76px;top:4740px" width="170" height="112" viewBox="0 0 170 112">
  <polygon points="85,6 164,56 85,106 6,56" fill="#fff" stroke="var(--orange)" stroke-width="6" stroke-linejoin="round"/>
</svg>
<div class="abs" style="left:76px;top:4782px;width:170px;text-align:center;font-size:14px;font-weight:700;color:var(--blue);line-height:15px">Coral Ridge<br>Pools</div>

<svg width="0" height="0" class="abs"><defs>
  <g id="footIcon"><polygon points="22,2 42,22 22,42 2,22" fill="#fff" stroke="var(--orange)" stroke-width="2" stroke-linejoin="round"/></g>
</defs></svg>
<div class="abs footer-item" style="left:290px;top:4777px">
  <svg width="44" height="44"><use href="#footIcon"/><path d="M16 15c1 6 5 11 12 13l2-3-3-2-2 1c-2-1-4-3-5-5l1-2-2-3z" fill="var(--blue)"/></svg>
  <div>CALL US<br>(702) 555-0148</div>
</div>
<div class="abs footer-item" style="left:512px;top:4777px">
  <svg width="44" height="44"><use href="#footIcon"/><rect x="14" y="16" width="16" height="12" rx="1" fill="var(--blue)"/><path d="M14 17l8 6 8-6" fill="none" stroke="#fff" stroke-width="1.4"/></svg>
  <div>EMAIL US<br>poolsolutions@coralridgepoolsqx.com</div>
</div>
<div class="abs footer-item" style="left:898px;top:4777px">
  <svg width="44" height="44"><use href="#footIcon"/><path d="M22 31s-7-7-7-12a7 7 0 0 1 14 0c0 5-7 12-7 12z" fill="var(--blue)"/><circle cx="22" cy="19" r="2.5" fill="#fff"/></svg>
  <div>Address line Dummy here<br>Address line Dummy here</div>
</div>
<div class="abs footer-rule" style="top:4879px"></div>
<div class="abs footer-links"><span>ABOUT US</span><span>|</span><span>OUR SERVICES</span><span>|</span><span>FREE ESTIMATES</span><span>|</span><span>BLOG</span><span>|</span><span>CONTACT US</span></div>
<div class="abs footer-rule" style="top:4948px"></div>
<div class="abs" style="left:60px;top:4980px;color:#fff;font-size:11px">Copyright © 2025 All Rights Reserved By Company name</div>
<div class="abs" style="left:1008px;top:4976px;display:flex;gap:6px">
  <div class="social"></div><div class="social"></div><div class="social"></div><div class="social"></div>
</div>

</body>
</html>
```